Financial Advisor Brochure to attract new clients

I am launching a new career as a Financial Advisor and a flier that shows what services I offer and why I decided to go back to work at this point in my life. I have a deep desire to help people meet their dreams and believe that a solid financial foundation provides the ability to live your life as you want to and not how you have to. I created a simple flier but know that so much more can be done to catch a persons eye.

Target Market(s)

Entrepeneurs and Woman in all stages of life.

Industry/Entity Type

Financial Advisor

Font styles to use
Sans Serif

Colors
00AB8E
00BBA5
67D7C9
C6EFE9
E9F9F6

Requirements
Must have
• my photo, contact information and Cobaltra Logo

```html
<!DOCTYPE html>
<html lang="en">
<head>
<meta charset="utf-8">
<title>Marla Quintero – Financial Advisor Profile</title>
<link href="https://fonts.googleapis.com/css2?family=Raleway:wght@400;500;600;700;800&display=swap" rel="stylesheet">
<style>
  :root{
    --brand-blue:#0b6cae;
    --brand-blue-deep:#0a5f9c;
    --pill-blue:#3db4f2;
    --accent-text:#1670b3;
    --panel-grey:#ececec;
    --footer-grey:#7d7b7b;
    --ink:#2b2b2b;
    --white:#ffffff;
    --bullet:#3a8fd0;
  }
  *{box-sizing:border-box;margin:0;padding:0}
  html,body{width:718px;height:1200px;overflow:hidden;background:var(--white)}
  body{font-family:'Raleway',Arial,sans-serif;color:var(--ink)}
  .flyer{position:relative;width:718px;height:1200px;overflow:hidden;background:var(--white)}

  /* header */
  .hero{position:absolute;left:0;top:0;width:718px;height:410px;
    background:radial-gradient(circle at 40% 40%,#1c80c2 0%,var(--brand-blue) 45%,var(--brand-blue-deep) 100%)}
  .hero-text{position:absolute;left:30px;top:58px;width:345px;text-align:center;color:var(--white)}
  .advisor-name{font-size:29px;font-weight:700;letter-spacing:.3px}
  .advisor-role{font-size:27px;font-weight:400;margin-top:8px}
  .profile-pill{display:inline-block;margin-top:12px;width:200px;height:40px;line-height:40px;border-radius:20px;
    background:var(--pill-blue);color:#143049;font-size:28px;font-weight:500}
  .tagline{width:300px;margin:22px auto 0;font-size:18px;line-height:26px;font-weight:400}
  .portrait{position:absolute;left:440px;top:18px;width:240px;height:392px;
    border-radius:120px 120px 0 0;
    background:linear-gradient(180deg,#8a5a3c 0%,#b98466 28%,#1b9a7c 52%,#0f7d63 100%)}

  /* intro panels */
  .intro-left{position:absolute;left:0;top:410px;width:718px;height:215px;background:var(--panel-grey)}
  .intro-right{position:absolute;left:383px;top:410px;width:335px;height:318px;background:var(--panel-grey);border-bottom-left-radius:12px}
  .intro-copy{position:absolute;font-size:11px;line-height:15px;font-family:Arial,Helvetica,sans-serif}
  .intro-copy p+p{margin-top:15px}
  .copy-left{left:50px;top:424px;width:305px}
  .copy-right{left:407px;top:424px;width:290px}

  /* services */
  .services-title{position:absolute;left:50px;top:640px;font-size:23px;font-weight:500;line-height:27px;color:#1d1d1d}
  .service{position:absolute}
  .service.col-left{width:225px}
  .service.col-right{width:235px}
  .service-icon{position:absolute;left:-60px;top:-6px;width:44px;height:44px}
  .service-name{font-size:17px;font-weight:500;color:#1d1d1d;white-space:nowrap}
  .service-name span{color:var(--accent-text)}
  .service-list{list-style:none;margin-top:10px;font-family:Arial,Helvetica,sans-serif;font-size:11px;line-height:15px}
  .service-list li{position:relative;padding-left:16px}
  .service-list li::before{content:"›";position:absolute;left:1px;top:-1px;width:9px;height:9px;border-radius:50%;
    color:var(--white);background:var(--bullet);font-size:9px;line-height:9px;text-align:center;margin-top:3px}

  /* footer */
  .contact-band{position:absolute;left:0;top:1124px;width:718px;height:76px;background:var(--footer-grey)}
  .call-tab{position:absolute;left:0;top:1095px;width:360px;height:105px;background:var(--brand-blue);
    border-top-right-radius:70px 60px;box-shadow:5px 0 0 #ffffff}
  .call-label{position:absolute;left:50px;top:1108px;font-size:17px;color:var(--white);letter-spacing:.3px}
  .call-number{position:absolute;left:85px;top:1132px;font-size:37px;font-weight:800;color:var(--white);letter-spacing:1px}
  .call-icon{position:absolute;left:48px;top:1142px;width:30px;height:30px}
  .contact-list{position:absolute;left:395px;top:1143px;list-style:none;font-size:13px;line-height:22px;color:var(--white)}
  .contact-list li{display:flex;align-items:center;gap:10px}
  .contact-list svg{width:15px;height:15px}
</style>
</head>
<body>
<main class="flyer">
  <header class="hero">
    <div class="hero-text">
      <h1 class="advisor-name">MARLA QUINTERO</h1>
      <p class="advisor-role">Financial Advisor</p>
      <div class="profile-pill">PROFILE</div>
      <p class="tagline">Passionate about helping empower you with knowledge to make informed financial decisions throughout all of life’s stages and help you achieve your goals.</p>
    </div>
    <div class="portrait" role="img" aria-label="Portrait photo of the advisor, smiling, wearing a green blouse, seated against a blue backdrop"></div>
  </header>

  <section class="intro-left"></section>
  <section class="intro-right"></section>
  <div class="intro-copy copy-left">
    <p>As a business owner, wife, and mother of two teenagers, I understand the struggles you face juggling your personal, business, and financial life.</p>
    <p>I grew up in a home where my parents had opposing money habits. My Dad was a big spender and mom was a saver. Through the years, I saw how my mom’s consistent savings grew while Dad’s style led to many financial ups and downs. This made a huge impression on me and sparked my continued interest in all things finance.</p>
  </div>
  <div class="intro-copy copy-right">
    <p>Having an entrepreneurial personality and ability to explain concepts in a relatable manner has provided me with many opportunities. In 2018, After decades of running a sales agency, I sold my company to spend time with my kids and family but my interest in Finance never waned. Now that our kids are thriving teenagers, I started a new career as a licensed Financial Advisor with a heart to help you achieve your financial dreams.</p>
    <p>The financial world is changing rapidly, and it can be confusing on how to maneuver through these times. My goal is to pull out the emotions that cloud judgement and help you make better decisions with your long-range goals in mind.</p>
  </div>

  <h2 class="services-title">Financial planning services<br>offered:</h2>

  <article class="service col-left" style="left:110px;top:738px">
    <svg class="service-icon" viewBox="0 0 44 44" fill="none" stroke="#222" stroke-width="2"><circle cx="22" cy="22" r="13"/><circle cx="22" cy="22" r="6"/><path d="M22 4v5M22 35v5M4 22h5M35 22h5M9 9l4 4M31 31l4 4M35 9l-4 4M9 35l4-4"/></svg>
    <h3 class="service-name">Transition <span>Planning</span></h3>
    <ul class="service-list"><li>Divorce planning.</li><li>Strategy and guidance pre, during, and post- divorce</li></ul>
  </article>

  <article class="service col-left" style="left:110px;top:845px">
    <svg class="service-icon" viewBox="0 0 44 44" fill="none" stroke="#222" stroke-width="2"><path d="M8 40V24h12l8 4v6H14M10 20l14-14h10v8L22 26"/><circle cx="30" cy="12" r="4"/></svg>
    <h3 class="service-name">Retirement <span>planning</span></h3>
    <ul class="service-list"><li>Current portfolio analysis</li><li>Timeline asset and income planning</li><li>Tax and estate review and projections</li></ul>
  </article>

  <article class="service col-left" style="left:110px;top:972px">
    <svg class="service-icon" viewBox="0 0 44 44" fill="none" stroke="#222" stroke-width="2"><path d="M22 4L6 18h32zM10 18v20h24V18"/><path d="M6 30l8-6 8 6 8-6 8 6"/></svg>
    <h3 class="service-name">Real estate <span>acquisition or sale</span></h3>
    <ul class="service-list"><li>Acquisition or dissolution of real estate. Individual or portfolio</li></ul>
  </article>

  <article class="service col-right" style="left:433px;top:748px">
    <svg class="service-icon" viewBox="0 0 44 44" fill="none" stroke="#222" stroke-width="2"><circle cx="22" cy="28" r="9"/><path d="M22 23v10M4 12l8-6 10 6 10-6 8 6"/></svg>
    <h3 class="service-name">Business <span>sale or purchase</span></h3>
    <ul class="service-list"><li>Company valuations</li><li>Tax impact analysis</li><li>Strategy implementation for funds received from sale</li></ul>
  </article>

  <article class="service col-right" style="left:433px;top:878px">
    <svg class="service-icon" viewBox="0 0 44 44" fill="none" stroke="#222" stroke-width="2"><rect x="14" y="4" width="18" height="24"/><path d="M18 10h3M25 10h3M18 16h3M25 16h3M4 32l10 6h16l10-8"/></svg>
    <h3 class="service-name">Estate <span>planning:</span></h3>
    <ul class="service-list"><li>Strategies for creating future generational wealth.</li></ul>
  </article>

  <article class="service col-right" style="left:433px;top:978px">
    <svg class="service-icon" viewBox="0 0 44 44" fill="none" stroke="#222" stroke-width="2"><path d="M4 30V20M10 30V16M16 30V22"/><circle cx="30" cy="14" r="6"/><path d="M20 40c0-8 5-12 10-12s10 4 10 12"/><circle cx="10" cy="38" r="4"/></svg>
    <h3 class="service-name">New <span>Investors:</span></h3>
    <ul class="service-list"><li>Assistance in opening investment and retirement acc</li></ul>
  </article>

  <footer>
    <div class="contact-band"></div>
    <div class="call-tab"></div>
    <p class="call-label">CALL FOR AN APPOINTMENT</p>
    <svg class="call-icon" viewBox="0 0 30 30" fill="none" stroke="#fff" stroke-width="1.8"><path d="M7 4l5 5-3 3c1 4 4 7 8 8l3-3 5 5-3 4C12 26 4 18 3 8z"/><path d="M18 6a7 7 0 0 1 6 6M18 2a11 11 0 0 1 10 10"/></svg>
    <p class="call-number">555-014-8263</p>
    <ul class="contact-list">
      <li><svg viewBox="0 0 16 16" fill="none" stroke="#fff" stroke-width="1.2"><rect x="1" y="3" width="14" height="10"/><path d="M1 3l7 6 7-6"/></svg>marla.quintero@cobaltrawealthalliance.com</li>
      <li><svg viewBox="0 0 16 16" fill="none" stroke="#fff" stroke-width="1.2"><circle cx="8" cy="8" r="7"/><ellipse cx="8" cy="8" rx="3" ry="7"/><path d="M1 8h14"/></svg>www.cobaltrawealthalliance.com</li>
    </ul>
  </footer>
</main>
</body>
</html>
```